Wine Label for a White and a Red Wine from Italy

We have a very good idea of what we want with artwork. We need you to please design a 'template' with the text so we can change out the artwork from year to year. Samples are shown of what we are looking for. We are looking for options with the two basic designs. Brand name of wine is: Valora di Castegno. Both wines are in a light green Bordeaux-style bottle (note: we don't show a light green bottle in the mockup but please remember the bottle is light green). Artwork is provided. We'd like to see either the green or blue butterfly on the white wine, the red butterfly is for the red wine. Please base the design on the attached label from Brailey and/or the attached label from Chateau Mervanges.

Target Market(s)

Millennials, women

Requirements
Must have
• The artwork (butterflies) attached.
Nice to have
• Elegant, readable fonts. Please make the text so it can be changed by the printer. Please make it so the artwork can be changed too.

```html
<!DOCTYPE html>
<html lang="en">
<head>
<meta charset="utf-8">
<title>Valora di Castegno – Barrel Select Labels</title>
<link rel="stylesheet" href="https://fonts.googleapis.com/css2?family=Marcellus&family=Montserrat:wght@500&family=Poppins:wght@400&display=swap">
<style>
  :root{
    --page:#ffffff;
    --label:#fdfcf6;
    --green:#1f5c53;
    --red:#8e1d26;
    --gold:#c5a15c;
    --amber:#e9a321;
    --amber-light:#f6c94a;
    --teal:#1f8d8c;
    --crimson:#b32a22;
    --ink-soft:#b69a63;
  }
  *{margin:0;padding:0;box-sizing:border-box}
  html,body{width:1200px;height:1200px;overflow:hidden;background:var(--page)}
  .canvas{position:relative;width:1200px;height:1200px}
  .label{
    position:absolute;top:211px;width:520px;height:777px;
    background:var(--label);
    box-shadow:0 1px 4px rgba(0,0,0,.18);
  }
  .label--bianco{left:53px;--accent:var(--green)}
  .label--rosso{left:627px;--accent:var(--red)}

  .brand{position:absolute;left:0;right:0;top:52px;text-align:center;color:var(--accent);font-family:"Marcellus",serif}
  .brand__name{display:block;font-size:56px;line-height:1}
  .brand__region{display:block;font-size:26px;line-height:1;margin-top:8px;padding-left:120px}

  .range{
    position:absolute;left:0;right:0;top:180px;
    display:flex;justify-content:center;align-items:center;gap:10px;
    font-family:"Montserrat",sans-serif;font-weight:500;font-size:22px;letter-spacing:2px;color:var(--gold);
  }
  .range__dot{width:12px;height:12px;border-radius:50%;background:var(--accent)}

  .artwork{position:absolute;left:0;right:0;top:230px;height:388px}
  .label--bianco .artwork{background:radial-gradient(ellipse 45% 40% at 50% 45%, var(--teal) 0%, #1d5e5c 45%, var(--amber) 80%, var(--amber-light) 100%)}
  .label--rosso .artwork{background:radial-gradient(ellipse 50% 40% at 50% 42%, var(--crimson) 0%, #8a2017 45%, var(--amber) 82%, var(--amber-light) 100%)}

  .vintage{position:absolute;left:0;right:0;top:550px;text-align:center;font-family:"Marcellus",serif;font-size:56px;color:#fff;line-height:1}

  .wine{position:absolute;left:0;right:0;top:638px;text-align:center;font-family:"Marcellus",serif;color:var(--gold)}
  .wine__type{display:block;font-size:34px;line-height:1}
  .wine__origin{display:block;font-size:18px;margin-top:4px;color:var(--ink-soft)}

  .spec{position:absolute;top:668px;font-family:"Marcellus",serif;font-size:24px;color:var(--ink-soft)}
  .spec--abv{left:22px}
  .spec--volume{right:22px}

  .producer{position:absolute;left:0;right:0;top:706px;text-align:center;font-family:"Poppins",sans-serif;font-size:14px;line-height:23px;color:var(--accent)}
</style>
</head>
<body>
<main class="canvas">

  <section class="label label--bianco">
    <div class="brand"><span class="brand__name">Valora</span><span class="brand__region">di Castegno</span></div>
    <div class="range"><span>BARREL</span><span class="range__dot"></span><span>SELECT</span></div>
    <div class="artwork" role="img" aria-label="Painted teal butterfly on an amber and yellow brushstroke background"></div>
    <div class="vintage">2018</div>
    <div class="wine"><span class="wine__type">Rosso</span><span class="wine__origin">Piemonte, Italy</span></div>
    <span class="spec spec--abv">13,5%</span>
    <span class="spec spec--volume">75cl</span>
    <p class="producer">Artisanlly Crafted by Cantina Quattro Colli<br>sustainable farmed</p>
  </section>

  <section class="label label--rosso">
    <div class="brand"><span class="brand__name">Valora</span><span class="brand__region">di Castegno</span></div>
    <div class="range"><span>BARREL</span><span class="range__dot"></span><span>SELECT</span></div>
    <div class="artwork" role="img" aria-label="Painted red butterfly on an amber and yellow brushstroke background"></div>
    <div class="vintage">2018</div>
    <div class="wine"><span class="wine__type">Rosso</span><span class="wine__origin">Piemonte, Italy</span></div>
    <span class="spec spec--abv">13,5%</span>
    <span class="spec spec--volume">75cl</span>
    <p class="producer">Artisanlly Crafted by Cantina Quattro Colli<br>sustainable farmed</p>
  </section>

</main>
</body>
</html>
```